Redesign existing website

We would like a redesign of the website http://www.velbrisanalytics.com that creates a more modern, up to date look.

Velbris Analytics creates software for social science research and is focused on making the software user friendly and easy to use. We would like to convey seriousness, but also
a very up to date, just released look.

Feel free to modify the logo if you wish.

Target Market(s)

Academics, researchers

Industry/Entity Type

Software

Requirements
Must have
• The design should incorporate the same information as the current website.

```html
<!DOCTYPE html>
<html lang="en">
<head>
<meta charset="utf-8">
<title>Velbris Analytics</title>
<link href="https://fonts.googleapis.com/css2?family=Arimo:wght@400;700&family=Poiret+One&display=swap" rel="stylesheet">
<style>
  :root {
    --top-band: #c0c0c0;
    --hero-black: #000000;
    --body-grey: #202020;
    --footer-black: #0d0d0d;
    --nav-grey: #c8c8c8;
    --nav-text: #111111;
    --brand-blue: #2b4aa0;
    --white: #ffffff;
    --text-light: #e6e6e6;
    --green-top: #6cc31e;
    --green-bottom: #3f8f0c;
    --button-text: #0e1a05;
    --map-tone: #262626;
    --screen-light: #dfe8f4;
    --screen-dark: #7f9cc4;
  }
  * { box-sizing: border-box; margin: 0; padding: 0; }
  html, body { width: 1200px; height: 886px; overflow: hidden; background: var(--hero-black); }
  .page { position: relative; width: 1200px; height: 886px; font-family: "Arimo", Arial, sans-serif; }
  .top-band { position: absolute; left: 0; top: 0; width: 1200px; height: 68px; background: var(--top-band); }
  .hero { position: absolute; left: 0; top: 68px; width: 1200px; height: 389px; background: var(--hero-black); }
  .content-area { position: absolute; left: 0; top: 457px; width: 1200px; height: 372px; background: var(--body-grey); }
  .footer { position: absolute; left: 0; top: 829px; width: 1200px; height: 57px; background: var(--footer-black); }

  .world-map { position: absolute; left: 305px; top: 105px; width: 670px; height: 352px;
    background: radial-gradient(ellipse at 50% 45%, var(--map-tone) 0%, rgba(38,38,38,0.4) 55%, rgba(0,0,0,0) 75%); }

  .nav { position: absolute; display: flex; justify-content: space-around; align-items: center; background: var(--nav-grey); }
  .nav a { color: var(--nav-text); text-decoration: none; font-size: 13px; }
  .nav-top { left: 560px; top: 68px; width: 427px; height: 37px; }
  .nav-bottom { left: 408px; top: 850px; width: 424px; height: 36px; }

  .brand { position: absolute; left: 258px; top: 30px; width: 205px; text-align: center; }
  .brand-mark { display: block; margin: 0 auto; width: 94px; height: 94px; }
  .brand-name { display: block; margin-top: 4px; font-size: 22px; color: var(--brand-blue); white-space: nowrap; }

  .tagline { position: absolute; right: 227px; top: 218px; text-align: right; font-family: "Poiret One", sans-serif;
    font-size: 24px; line-height: 21px; color: var(--white); letter-spacing: 0.5px; }

  .screenshot { position: absolute; left: 211px; top: 314px; width: 330px; height: 237px;
    background: linear-gradient(160deg, var(--screen-light) 0%, var(--screen-dark) 100%); }
  .screenshot-reflection { position: absolute; left: 211px; top: 553px; width: 330px; height: 110px;
    background: linear-gradient(180deg, rgba(127,156,196,0.35) 0%, rgba(32,32,32,0) 100%); }

  .download-button { position: absolute; left: 689px; top: 396px; width: 305px; height: 85px; border-radius: 8px;
    background: linear-gradient(180deg, var(--green-top) 0%, var(--green-bottom) 100%);
    box-shadow: 0 12px 20px rgba(0,0,0,0.5);
    display: flex; align-items: center; justify-content: center; text-align: center;
    font-weight: 700; font-size: 22px; line-height: 21px; color: var(--button-text); text-decoration: none; }

  .mission { position: absolute; left: 330px; top: 658px; width: 620px; color: var(--text-light); font-size: 13px; line-height: 21px; }
  .mission p + p { margin-top: 22px; }
</style>
</head>
<body>
<div class="page">
  <div class="top-band"></div>
  <div class="hero"></div>
  <div class="content-area"></div>
  <div class="footer"></div>

  <div class="world-map" role="img" aria-label="Dark dotted world map behind the header"></div>

  <nav class="nav nav-top">
    <a href="#">Home</a><a href="#">Products</a><a href="#">News</a><a href="#">About Us</a><a href="#">Contact Us</a>
  </nav>

  <div class="brand">
    <svg class="brand-mark" viewBox="0 0 94 94" aria-hidden="true"><circle cx="47" cy="47" r="44" fill="#2b4aa0"/></svg>
    <span class="brand-name">Velbris Analytics</span>
  </div>

  <div class="tagline">Increasing the power and<br>efficiency of empirical<br>social science research</div>

  <div class="screenshot" role="img" aria-label="Screenshot of the population and health data manager software"></div>
  <div class="screenshot-reflection" aria-hidden="true"></div>

  <a class="download-button" href="#">Download Preview<br>Release</a>

  <div class="mission">
    <p>The mission of Velbris Analytics, Inc. is to produce software products that multiply the power and efficiency of empirical scientific research in the social sciences.</p>
    <p>A central goal is to expand access to complex data sources and to the advanced methods<br>of scientific investigation needed to analyze them.</p>
  </div>

  <nav class="nav nav-bottom">
    <a href="#">Home</a><a href="#">Products</a><a href="#">News</a><a href="#">About Us</a><a href="#">Contact Us</a>
  </nav>
</div>
</body>
</html>
```